Venlox - Property Management Company Listings - PSD / uncoded only

Our site simply connects property owners with property managers. I’m asking you to create 2 pages, 1 homepage and 1 page that lists of property management companies. Build with Responsive Design in mind. PSD/uncoded files only. Help us create a great site!
Example competitor sites:
http://www.everyestatehelp.example/
http://www.tendyourlots.example/
Inspired by these sites:
http://www.quorvik.example/
http://www.bespokely.example/
http://www.coinwire.example/
https://www.tripboard.example/
I've attached the logo as well as 2 picture files that you can consider using.
• Venlox Logo Colors: Yellow: HTML code: #FBC30A, RGB code: R: 251 G: 195 B: 10 Grey: HTML code: #4E4C4D, RGB code: R: 78 G: 76 B: 77
• The picture files are optional.
o One picture is of houses and neighborhood.
o The other is of a professional woman on the phone. Please do not use the professional woman as a large primary image. You can use the professional woman photo as a smaller photo and not the main photo.
• Please bring your own pictures and graphics too. Don't feel like you need to use mine.
Thank you!

```html
<!DOCTYPE html>
<html lang="en">
<head>
<meta charset="utf-8">
<title>Venlox – Find your Local Property Manager</title>
<link href="https://fonts.googleapis.com/css2?family=Roboto+Condensed:wght@400;700&family=Open+Sans:ital,wght@0,400;0,600;0,700;1,700&family=Caveat&display=swap" rel="stylesheet">
<style>
:root{
  --yellow:#fbc30a;
  --yellow-deep:#f2b200;
  --grey:#4e4c4d;
  --ink:#222222;
  --text:#555555;
  --muted:#8a8a8a;
  --line:#e2e2e2;
  --dark:#1d1d1d;
  --dark-tab:#3b3b3b;
  --soft:#efefef;
  --white:#ffffff;
}
*{margin:0;padding:0;box-sizing:border-box}
html,body{width:1200px;height:3267px;overflow:hidden}
body{position:relative;background:var(--white);font-family:"Open Sans",Arial,sans-serif;color:var(--text)}
.abs{position:absolute}

/* hero */
.hero{position:absolute;left:0;top:0;width:1200px;height:736px;background:linear-gradient(90deg,#f3f2f0 0%,#e9e8e5 45%,#dcdad6 100%)}
.hero-photo{position:absolute;left:850px;top:0;width:350px;height:736px;background:linear-gradient(180deg,#d8d2cc 0%,#b98f74 45%,#8a8a8c 100%)}
.brand{position:absolute;left:98px;top:28px;display:flex;align-items:center;gap:10px}
.brand-mark{width:22px;height:22px;background:var(--yellow)}
.brand-name{font-family:"Open Sans",sans-serif;font-weight:700;font-size:46px;color:var(--grey);line-height:1}
.call{position:absolute;right:110px;top:26px;font-family:"Roboto Condensed",sans-serif;font-weight:700;font-size:20px;color:var(--ink)}
.nav{position:absolute;right:110px;top:74px;display:flex;align-items:center;gap:26px;font-family:"Roboto Condensed",sans-serif;font-size:15px;color:var(--ink)}
.nav .contact{border:2px solid var(--white);color:var(--white);padding:8px 20px;background:rgba(255,255,255,.08)}
.hero-title{position:absolute;left:111px;top:296px;font-family:"Roboto Condensed",sans-serif;font-weight:700;line-height:1.2}
.hero-title .l1{font-size:50px;color:var(--ink);display:block}
.hero-title .l2{font-size:48px;color:var(--yellow);display:block}
.hero-copy{position:absolute;left:111px;top:436px;width:600px;font-size:12.5px;line-height:1.6;color:#333}
.search{position:absolute;left:111px;top:516px;display:flex;align-items:center;height:56px}
.search .select{width:281px;height:56px;background:var(--white);border:1px solid #ddd;display:flex;align-items:center;justify-content:space-between;font-size:14px;color:#aaa;font-weight:600}
.search .select span{padding-left:14px}
.search .select i{width:50px;height:54px;background:var(--yellow);display:flex;align-items:center;justify-content:center}
.search .zip{margin-left:14px;width:174px;height:56px;background:#3a3a3a;color:var(--white);font-family:"Roboto Condensed",sans-serif;font-weight:700;font-size:20px;display:flex;align-items:center;justify-content:center}
.search .go{margin-left:22px;font-family:"Roboto Condensed",sans-serif;font-weight:700;font-size:23px;color:var(--ink);text-decoration:underline}
.hint{position:absolute;left:405px;top:598px;font-family:"Caveat",cursive;font-size:22px;color:#888}

/* feature tabs */
.tabs{position:absolute;left:0;top:736px;width:1200px;height:129px;background:var(--dark)}
.tab{position:absolute;top:0;width:231px;height:129px;text-align:center;font-family:"Roboto Condensed",sans-serif;font-size:13px;color:#7d7d7d;line-height:1.2;padding-top:22px}
.tab svg{display:block;margin:0 auto 8px}
.tab.active{background:var(--dark-tab);color:var(--white);font-size:15px}
.tab.active::before{content:"";position:absolute;left:50%;top:-18px;margin-left:-18px;border:18px solid transparent;border-top:0;border-bottom:18px solid var(--dark-tab)}

/* manager call */
.manager{position:absolute;left:0;top:865px;width:1200px;height:477px;text-align:center}
.manager .badge{position:absolute;left:562px;top:115px}
.manager h2{position:absolute;left:0;width:1200px;top:218px;font-weight:400;font-size:30px;color:var(--ink);letter-spacing:.5px}
.manager h2 b{font-weight:700}
.manager p{position:absolute;left:300px;width:600px;top:268px;font-size:13.5px;line-height:1.55;color:#666}
.btn{display:inline-flex;align-items:center;justify-content:center;background:var(--yellow);color:var(--white);font-weight:700;font-size:15px}
.manager .btn{position:absolute;left:529px;top:326px;width:142px;height:44px;box-shadow:0 2px 0 var(--yellow-deep)}

/* who we are */
.about{position:absolute;left:0;top:1342px;width:1200px;height:531px;background:linear-gradient(90deg,#f7f7f7,#ececec)}
.about-art{position:absolute;left:0;top:0;width:545px;height:531px;background:radial-gradient(ellipse at 45% 60%,#d9b7a0 0%,#ece6e0 50%,#f4f4f4 80%)}
.about h2{position:absolute;left:599px;top:82px;font-weight:400;font-size:31px;color:var(--ink)}
.about p{position:absolute;left:599px;top:136px;width:480px;font-size:12.8px;line-height:1.6;color:#444}
.about .rail{position:absolute;left:605px;top:370px;width:485px;height:2px;background:#cfcfcf}
.about .rail::before,.about .rail::after{content:"";position:absolute;top:-18px;width:2px;height:38px;background:#cfcfcf}
.about .rail::before{left:0}.about .rail::after{right:0}
.point{position:absolute;top:341px;width:120px;margin-left:-60px;text-align:center;font-size:12.5px;color:#333}
.point .ring{width:60px;height:60px;border-radius:50%;border:2px solid #d0d0d0;background:#f2f2f2;margin:0 auto 10px;display:flex;align-items:center;justify-content:center}

/* featured properties */
.featured{position:absolute;left:0;top:1873px;width:1200px;height:860px}
.featured .icon{position:absolute;left:570px;top:135px}
.featured h2{position:absolute;left:0;width:1200px;top:200px;text-align:center;font-weight:400;font-size:29px;color:var(--ink);letter-spacing:.5px}
.filters{position:absolute;left:364px;top:262px;display:flex;gap:0;font-size:13px;color:#333}
.filters span{padding:8px 16px}
.filters .on{background:#e6e6e6}
.featured .shade{position:absolute;left:150px;top:312px;width:900px;height:10px;background:radial-gradient(ellipse at 50% 0,rgba(0,0,0,.12),rgba(0,0,0,0) 70%)}
.card{position:absolute;top:375px;width:270px;height:361px;background:var(--white);border:1px solid var(--line)}
.card .photo{position:relative;height:184px}
.card .sale{position:absolute;right:0;bottom:0;background:var(--yellow);color:var(--ink);font-weight:700;font-size:11.5px;padding:8px 11px}
.card h3{position:absolute;left:16px;top:200px;font-weight:400;font-size:14.5px;color:#222}
.card .heart{position:absolute;right:16px;top:202px}
.card .city{position:absolute;left:16px;top:228px;font-size:11px;color:#999}
.card .divider{position:absolute;left:16px;right:16px;top:250px;height:1px;background:var(--line)}
.card .price{position:absolute;left:0;width:100%;top:265px;text-align:center;font-weight:600;font-size:29px;color:var(--yellow)}
.card .price small{font-size:20px}
.card .specs{position:absolute;left:0;bottom:0;width:100%;height:40px;border-top:1px solid var(--line);display:flex;font-size:11px;color:#444}
.card .specs div{flex:1;display:flex;align-items:center;gap:8px;padding-left:14px;border-right:1px solid var(--line)}
.card .specs div:last-child{border-right:0}

/* contact */
.contact{position:absolute;left:0;top:2733px;width:1200px;height:490px;background:var(--dark);color:var(--white)}
.contact h2{position:absolute;left:0;width:1200px;top:44px;text-align:center;font-weight:400;font-size:29px}
.call-box{position:absolute;left:157px;top:133px;width:388px;height:283px;border:2px solid #cfcfcf;text-align:center}
.call-box svg{margin-top:62px}
.call-box .now{font-size:30px;color:var(--yellow);margin-top:6px}
.call-box .num{font-size:27px;font-weight:600;margin-top:2px}
.quote{position:absolute;left:577px;top:133px;width:464px}
.quote h3{font-style:italic;font-weight:700;font-size:15px}
.quote p{font-size:11.5px;line-height:1.5;color:#ccc;margin-top:8px}
.field{height:41px;background:var(--white);color:#777;font-size:12px;padding:12px 14px;margin-top:16px}
.field:first-of-type{margin-top:16px}
.quote .btn{position:absolute;right:0;top:396px;width:109px;height:36px;color:var(--ink);font-size:16px}
.footer{position:absolute;left:0;top:3223px;width:1200px;height:44px;text-align:center;font-size:12px;color:#555;line-height:44px}
</style>
</head>
<body>

<header class="hero">
  <div class="hero-photo" role="img" aria-label="Smiling woman holding a small model house"></div>
  <div class="brand"><span class="brand-mark"></span><span class="brand-name">Venlox</span></div>
  <div class="call">CALL: 1800 555 014</div>
  <nav class="nav"><span>HOME</span><span>ARE YOU A PROPERTY MANAGER?</span><span class="contact">CONTACT</span></nav>
  <h1 class="hero-title"><span class="l1">Find your Local</span><span class="l2">PROPERTY MANAGER</span></h1>
  <p class="hero-copy">Neque porro quisquam est qui dolorem ipsum quia dolor sit amet, consectetur, adipisci velit..."There is no one who loves pain itself, who seeks after it and wants to have it, simply because it is pain..."</p>
  <div class="search">
    <div class="select"><span>select your property type</span><i><svg width="20" height="12" viewBox="0 0 20 12"><path d="M2 2l8 8 8-8" fill="none" stroke="#fff" stroke-width="3"/></svg></i></div>
    <div class="zip">Enter ZIP Code</div>
    <div class="go">SEARCH</div>
  </div>
  <div class="hint">will inform you in one min</div>
  <svg class="abs" style="left:630px;top:560px" width="30" height="50" viewBox="0 0 30 50"><path d="M4 46 C22 40 24 20 16 6" fill="none" stroke="#999" stroke-width="1.5"/><path d="M10 10 L16 4 L20 12" fill="none" stroke="#999" stroke-width="1.5"/></svg>
</header>

<section class="tabs">
  <div class="tab active" style="left:111px">
    <svg width="40" height="48" viewBox="0 0 40 48"><rect x="6" y="3" width="28" height="40" fill="none" stroke="#fff" stroke-width="2.5"/><path d="M12 14h16M12 22h16M12 30h10" stroke="#fff" stroke-width="2.5"/></svg>
    FEATURED<br>LISTING</div>
  <div class="tab" style="left:298px">
    <svg width="44" height="48" viewBox="0 0 44 48"><circle cx="25" cy="18" r="12" fill="none" stroke="#7d7d7d" stroke-width="2.5"/><path d="M16 27L5 40" stroke="#7d7d7d" stroke-width="4"/></svg>
    ADVANCE<br>SEARCH</div>
  <div class="tab" style="left:484px">
    <svg width="44" height="48" viewBox="0 0 44 48"><path d="M6 22L22 8l16 14" fill="none" stroke="#7d7d7d" stroke-width="2.5"/><rect x="12" y="22" width="20" height="18" fill="none" stroke="#7d7d7d" stroke-width="2.5"/></svg>
    PROVIDING PROPERT<br>MANAGEMENT</div>
  <div class="tab" style="left:691px">
    <svg width="50" height="48" viewBox="0 0 50 48"><rect x="8" y="10" width="34" height="26" fill="none" stroke="#7d7d7d" stroke-width="2.5"/><path d="M8 36l10-10h14l10 10" fill="none" stroke="#7d7d7d" stroke-width="2.5"/></svg>
    CONNECTING<br>PROPERTY OWNERS</div>
  <div class="tab" style="left:883px">
    <svg width="44" height="48" viewBox="0 0 44 48"><circle cx="22" cy="14" r="8" fill="#7d7d7d"/><path d="M6 42c0-12 8-18 16-18s16 6 16 18z" fill="#7d7d7d"/></svg>
    PROPERTY<br>MANAGER</div>
</section>

<section class="manager">
  <svg class="badge" width="76" height="76" viewBox="0 0 76 76"><circle cx="38" cy="38" r="36" fill="#d6d6d6"/><circle cx="38" cy="38" r="29" fill="none" stroke="#fff" stroke-width="3"/><path d="M22 38L38 24l16 14" fill="none" stroke="#fff" stroke-width="4"/><rect x="29" y="38" width="18" height="14" fill="#fff"/></svg>
  <h2>ARE YOU A <b>PROPERTY MANAGER?</b></h2>
  <p>Join our real estate property management company network. Let us help you find leads of property owners seeking to rent their homes.</p>
  <span class="btn">LEARN MORE</span>
</section>

<section class="about">
  <div class="about-art" role="img" aria-label="Happy family lying together framed by a yellow house outline"></div>
  <h2>Who we are?</h2>
  <p>Lorem Ipsum is simply dummy text of the printing and typesetting industry. Lorem Ipsum has been the industry's standard dummy text ever since the 1500s, when an unknown printer took a galley of type and scrambled it to make a type specimen book. It has survived not only five centuries, but also the leap into electronic typesetting, remaining essentially unchanged. It was popularised in the 1960s with the release of Glyphset sheets containing Lorem Ipsum passages, and more recently with desktop publishing software like Pagecraft Pro including versions of Lorem Ipsum.</p>
  <div class="rail"></div>
  <div class="point" style="left:671px"><div class="ring"><svg width="26" height="26" viewBox="0 0 26 26"><rect x="4" y="4" width="18" height="18" fill="none" stroke="#888" stroke-width="2"/><path d="M8 10h10M8 15h10" stroke="#888" stroke-width="2"/></svg></div>Lorem Lipsum</div>
  <div class="point" style="left:784px"><div class="ring"><svg width="30" height="20" viewBox="0 0 30 20"><path d="M1 10h7l3-8 4 16 3-8h11" fill="none" stroke="#888" stroke-width="2"/></svg></div>Lorem Lipsum</div>
  <div class="point" style="left:895px"><div class="ring"><svg width="26" height="26" viewBox="0 0 26 26"><rect x="4" y="16" width="4" height="7" fill="#888"/><rect x="11" y="11" width="4" height="12" fill="#888"/><rect x="18" y="5" width="4" height="18" fill="#888"/></svg></div>Lorem Lipsum</div>
  <div class="point" style="left:1008px"><div class="ring"><svg width="26" height="26" viewBox="0 0 26 26"><path d="M6 22c10-2 2-10 14-18" fill="none" stroke="#888" stroke-width="4"/></svg></div>Lorem Lipsum</div>
</section>

<section class="featured">
  <svg class="icon" width="60" height="54" viewBox="0 0 60 54"><path d="M4 28L30 4l26 24" fill="none" stroke="#111" stroke-width="6"/><path d="M12 26v26h14V38h8v14h14V26L30 10z" fill="#111"/></svg>
  <h2>FEATURED PROPERTIES</h2>
  <div class="filters"><span class="on">All</span><span>Apartments</span><span>Bungalows</span><span>Condominium</span><span>Villas</span></div>
  <div class="shade"></div>

  <article class="card" style="left:157px">
    <div class="photo" role="img" aria-label="White two-storey house with green lawn" style="background:linear-gradient(180deg,#4f7e3b 0%,#cfd3d4 45%,#6f8f4a 100%)"><span class="sale">FOR SALE</span></div>
    <h3>Harbor 7, Elmcrest, FL</h3>
    <svg class="heart" width="16" height="14" viewBox="0 0 16 14"><path d="M8 14L1 7a4 4 0 0 1 7-5 4 4 0 0 1 7 5z" fill="#777"/></svg>
    <div class="city">Miami</div><div class="divider"></div>
    <div class="price"><small>$</small>36000</div>
    <div class="specs"><div><svg width="14" height="14"><rect x="1" y="1" width="12" height="12" fill="none" stroke="#999"/></svg>240M</div><div><svg width="16" height="12"><rect x="1" y="4" width="14" height="6" fill="none" stroke="#999"/></svg>3</div><div><svg width="16" height="12"><path d="M1 11V2M1 7h14v4" fill="none" stroke="#999"/></svg>5</div></div>
  </article>

  <article class="card" style="left:457px">
    <div class="photo" role="img" aria-label="Blue-roofed white villa under a clear sky" style="background:linear-gradient(180deg,#5aa0e0 0%,#9fc4ea 40%,#e8e8ea 70%,#7a9a55 100%)"><span class="sale">FOR SALE</span></div>
    <h3>4120 Willow Avenue, Baywalk</h3>
    <svg class="heart" width="16" height="14" viewBox="0 0 16 14"><path d="M8 14L1 7a4 4 0 0 1 7-5 4 4 0 0 1 7 5z" fill="#777"/></svg>
    <div class="city">Miami</div><div class="divider"></div>
    <div class="price"><small>$</small>36000</div>
    <div class="specs"><div><svg width="14" height="14"><rect x="1" y="1" width="12" height="12" fill="none" stroke="#999"/></svg>250 M</div><div><svg width="16" height="12"><rect x="1" y="4" width="14" height="6" fill="none" stroke="#999"/></svg>4</div><div><svg width="16" height="12"><path d="M1 11V2M1 7h14v4" fill="none" stroke="#999"/></svg>4</div></div>
  </article>

  <article class="card" style="left:758px">
    <div class="photo" role="img" aria-label="Modern two-storey villa with tropical garden" style="background:linear-gradient(180deg,#6ea6d6 0%,#c9b48f 45%,#8a6f4d 70%,#5f8a3c 100%)"><span class="sale">FOR SALE</span></div>
    <h3>1850 Marlowe Avenue, Cora...</h3>
    <svg class="heart" width="16" height="14" viewBox="0 0 16 14"><path d="M8 14L1 7a4 4 0 0 1 7-5 4 4 0 0 1 7 5z" fill="#777"/></svg>
    <div class="city">Miami</div><div class="divider"></div>
    <div class="price"><small>$</small>36000</div>
    <div class="specs"><div><svg width="14" height="14"><rect x="1" y="1" width="12" height="12" fill="none" stroke="#999"/></svg>200M</div><div><svg width="16" height="12"><rect x="1" y="4" width="14" height="6" fill="none" stroke="#999"/></svg>3</div><div><svg width="16" height="12"><path d="M1 11V2M1 7h14v4" fill="none" stroke="#999"/></svg>4</div></div>
  </article>
</section>

<section class="contact">
  <h2>CONTACT US</h2>
  <div class="call-box">
    <svg width="48" height="48" viewBox="0 0 48 48"><path d="M12 6l8 8-5 5c3 6 8 11 14 14l5-5 8 8-6 6C22 42 6 26 6 12z" fill="#fff"/><path d="M28 8a12 12 0 0 1 12 12M28 14a6 6 0 0 1 6 6" fill="none" stroke="#fff" stroke-width="2.5"/></svg>
    <div class="now">Call Now</div>
    <div class="num">555 0198 321</div>
  </div>
  <form class="quote">
    <h3>GET A FREE QUOTE</h3>
    <p>Neque porro quisquam est qui dolorem ipsum quia dolor sit amet, consectetur, adipisci velit...</p>
    <div class="field">Full Name</div>
    <div class="field">Email</div>
    <div class="field">Phone Number</div>
    <div class="field">ZIP Code</div>
    <span class="btn">SEND</span>
  </form>
</section>

<footer class="footer">Copyright © 2014 Venlox. All rights reserved. | Terms Of Service | Privacy Policy</footer>

</body>
</html>
```